ROVA Pty Ltd Business Card

Looking for a simple yet eye-catching double-sided business card design using my company logo on one side and contact details on the other.

Target Market(s)

Government

Industry/Entity Type

Communication Systems Engineering

Contact Information for Business Card

ROVA Pty Ltd

Requirements
Nice to have
• Would be great to have a QR code so details can be scanned into contacts

```html
<!DOCTYPE html>
<html lang="en">
<head>
<meta charset="utf-8">
<title>ROVA Pty Ltd – Business Card</title>
<link href="https://fonts.googleapis.com/css2?family=Roboto:wght@400;500;700&display=swap" rel="stylesheet">
<style>
  :root {
    --page-bg: #d9d6d2;
    --card-top: #f1f0ee;
    --card-bottom: #e2e0dd;
    --panel-dark: #3a3d41;
    --panel-mid: #4a4e53;
    --ink: #2a2b2d;
    --ink-soft: #55585c;
  }
  * { box-sizing: border-box; margin: 0; padding: 0; }
  html, body {
    width: 1200px; height: 969px; overflow: hidden;
    background: var(--page-bg);
    font-family: "Roboto", Arial, sans-serif;
    color: var(--ink);
  }
  .card {
    position: absolute; left: 50px; top: 171px;
    width: 1100px; height: 626px;
    border-radius: 26px; overflow: hidden;
    background: linear-gradient(160deg, var(--card-top), var(--card-bottom));
    box-shadow: 0 10px 30px rgba(0,0,0,.18);
  }
  .circuit-art {
    position: absolute; left: 0; top: 0; width: 520px; height: 100%;
    background: linear-gradient(175deg, var(--panel-mid), var(--panel-dark));
    clip-path: polygon(0 0, 395px 0, 395px 80px, 450px 140px, 450px 245px, 345px 340px, 345px 415px, 250px 470px, 250px 100%, 0 100%);
  }
  .details {
    position: absolute; right: 86px; top: 0; text-align: right;
  }
  .brand {
    position: absolute; right: 0; top: 112px;
    display: flex; align-items: center; gap: 22px;
    white-space: nowrap;
  }
  .brand-dot { width: 26px; height: 26px; border-radius: 50%; background: var(--ink); }
  .brand-name { font-size: 76px; font-weight: 500; letter-spacing: 6px; line-height: 1; }
  .person-name {
    position: absolute; right: 0; top: 258px; white-space: nowrap;
    font-size: 38px; font-weight: 700; line-height: 1;
  }
  .person-title {
    position: absolute; right: 0; top: 314px; white-space: nowrap;
    font-size: 24px; color: var(--ink-soft); line-height: 1;
  }
  .address {
    position: absolute; right: 0; top: 378px; white-space: nowrap;
    font-size: 26px; line-height: 34px;
  }
  .contacts {
    position: absolute; right: 0; top: 478px; list-style: none; white-space: nowrap;
    font-size: 24px; line-height: 33px;
  }
  .contacts li { display: flex; justify-content: flex-end; align-items: center; gap: 16px; }
  .contacts svg { width: 20px; height: 20px; fill: var(--ink); }
</style>
</head>
<body>
  <div class="card">
    <div class="circuit-art" role="img" aria-label="Tree-shaped circuit board pattern in silver on dark grey"></div>
    <div class="details">
      <div class="brand">
        <span class="brand-dot"></span>
        <span class="brand-name">ROVA</span>
      </div>
      <p class="person-name">Daniel Morris</p>
      <p class="person-title">Managing Director</p>
      <p class="address">2190 Wattle Grove Road<br>Darwin, Northern Territory 0800</p>
      <ul class="contacts">
        <li>555-204-7781
          <svg viewBox="0 0 24 24"><path d="M6.6 10.8a15.1 15.1 0 0 0 6.6 6.6l2.2-2.2a1 1 0 0 1 1-.25 11.4 11.4 0 0 0 3.6.6 1 1 0 0 1 1 1V20a1 1 0 0 1-1 1A17 17 0 0 1 3 4a1 1 0 0 1 1-1h3.5a1 1 0 0 1 1 1c0 1.25.2 2.45.6 3.6a1 1 0 0 1-.25 1z"/></svg>
        </li>
        <li>info@rovasys.org
          <svg viewBox="0 0 24 24"><path d="M2 5h20v14H2z M3.5 6.5 12 13l8.5-6.5" fill="none" stroke="#2a2b2d" stroke-width="2"/></svg>
        </li>
        <li>www.rovasys.org
          <svg viewBox="0 0 24 24"><circle cx="12" cy="12" r="10"/><path d="M2 12h20M12 2c3 3 3 17 0 20M12 2c-3 3-3 17 0 20" fill="none" stroke="#f1f0ee" stroke-width="1.5"/></svg>
        </li>
      </ul>
    </div>
  </div>
</body>
</html>
```